Mapleton Drift Hire DL Flyer Design

I run a Ski and Snowboard hire shop in Australia, I am looking for a clean, simple and aesthetically pleasing way to display all of our hire prices for our different products.
The format will be DL double sided flyer, no folds, and we want it to align with our stores branding. Examples of our branding are as follows
< www.mapletondrift.com.au > and < www.mapletondrifthire.com.au >
I will also attach some screenshots below of some of the webpages.

Font should be "Poppins regular 400" available on google fonts, and titles and subtitles should be in all capitals.

I would like to have a QR code on the front side of the DL flyer that will go to < www.mapletondrifthire.com.au > and I would like it to be stylised in an appealing way. It should also be advertised that booking online will provide the user with a 25% discount.

The front of the pamphlet should be black and white only, and the back of the pamphlet can have a splash of colour that align with our branding.

Colour Pallet should include
#ff3399 (pink) or #34ccff (light blue) or #ff9933 (Orange)
#FFFFFF (white)
#000000 (black)

Overall I want the pamphlet to be crisp with hard lines, good formatting and easy to read for our customers.

I have attached our previous flyer only as a reference for how to lay out the prices on the backside of the flyer. I do not want to copy the front design at all.

I will need the source files of the project for future editing if prices change again.

I have attached our store logo.

I have attached our hire prices in an excel spreadsheet.

I have attached 2 screenshots of our retail website and 2 screenshots of our hire website for design/branding references.

Industry/Entity Type

Ski and Snowboard Hire

Font styles to use
Other font styles liked:
• Poppins Regular 400

Requirements
Must have
• Mapleton Drift Hire logo, either black on white logo or white on black logo depending on the design of the rest of the flyer. It must have a QR Code worked into the front design (QR Code should link to www.mapletondrifthire.com.au), must be in DL Flyer formate, double sided. The back of the flyer must display our prices
Nice to have
• Options for clean cut designs without pictures of snowboarders as well as some designs with a snowboarder.
Should not have
• The qr code in the example flyer, this QR code has been discontinued, it must be a newly generated QR Code

```html
<!DOCTYPE html>
<html lang="en">
<head>
<meta charset="utf-8">
<title>Mapleton Drift Hire – Hire Prices</title>
<link href="https://fonts.googleapis.com/css2?family=Poppins:wght@400;800;900&display=swap" rel="stylesheet">
<style>
  :root {
    --orange: #ff9933;
    --pink: #ff3399;
    --blue: #34ccff;
    --white: #ffffff;
    --black: #000000;
    --rule: #111111;
  }
  * { box-sizing: border-box; margin: 0; padding: 0; }
  html, body {
    width: 1200px; height: 2545px; overflow: hidden;
    background: var(--white);
    font-family: 'Poppins', sans-serif;
    color: var(--black);
  }
  .flyer { position: relative; width: 1200px; height: 2545px; }

  .price-table { position: absolute; left: 122px; width: 948px; font-size: 21.5px; }
  .price-table.adult { top: 154px; }
  .price-table.child { top: 1253px; }

  .row { display: grid; height: 40px; align-items: center; border-bottom: 2px solid var(--rule); }
  .adult .row { grid-template-columns: 414px 96px 96px 107px 116px 119px; }
  .child .row { grid-template-columns: 368px 82px 84px 92px 102px 105px 115px; }
  .row span { text-align: center; }
  .row span:first-child { text-align: left; }

  .table-head { height: 37px; border-bottom: none; color: var(--white); font-size: 23px; }
  .adult .table-head { background: var(--orange); }
  .child .table-head { background: var(--pink); color: var(--black); }
  .table-head span:first-child { padding-left: 12px; }
  .child .table-head span:first-child { padding-left: 10px; }

  .group { margin-top: 38px; border-top: 2px solid var(--rule); }
  .group.first { margin-top: 0; border-top: none; }
  .group.last .row:last-child { border-bottom: none; }

  .offer-band {
    position: absolute; left: 0; top: 2065px; width: 1200px; height: 480px;
    background: var(--black); border-top: 21px solid var(--orange);
    text-align: center;
  }
  .offer-lead {
    margin-top: 34px; color: var(--white); font-weight: 800;
    font-size: 50px; letter-spacing: 0.5px; line-height: 1;
  }
  .offer-value {
    margin-top: 12px; color: var(--orange); font-weight: 900;
    font-size: 113px; letter-spacing: -1px; line-height: 1;
  }
  .brand-row {
    position: absolute; left: 0; top: 300px; width: 1200px; height: 100px;
    display: grid; grid-template-columns: repeat(3, 1fr); align-items: center;
  }
  .brand-mark {
    display: flex; align-items: center; justify-content: center; gap: 16px;
    font-weight: 400; font-size: 32px; line-height: 1.15; text-align: left;
  }
  .brand-dot { width: 30px; height: 30px; border-radius: 50%; flex: none; }
  .brand-mark.pink { color: var(--pink); }
  .brand-mark.white { color: var(--white); }
  .brand-mark.blue { color: var(--blue); }
  .brand-mark.pink .brand-dot { background: var(--pink); }
  .brand-mark.white .brand-dot { background: var(--white); }
  .brand-mark.blue .brand-dot { background: var(--blue); }
</style>
</head>
<body>
<main class="flyer">

  <section class="price-table adult">
    <div class="row table-head"><span>Adult</span><span>1 Day</span><span>2 Day</span><span>3 Day</span><span>4/5 Day</span><span>6/7 Day</span></div>
    <div class="group first">
      <div class="row"><span>Board &amp; Boots Standard</span><span>60</span><span>90</span><span>110</span><span>120</span><span>140</span></div>
      <div class="row"><span>Board &amp; Boots Premium</span><span>80</span><span>110</span><span>130</span><span>150</span><span>180</span></div>
      <div class="row"><span>Board &amp; Boots Advanced</span><span>100</span><span>140</span><span>170</span><span>200</span><span>230</span></div>
      <div class="row"><span>Board Only Standard</span><span>50</span><span>75</span><span>95</span><span>110</span><span>125</span></div>
      <div class="row"><span>Board Only Premium</span><span>65</span><span>95</span><span>115</span><span>135</span><span>150</span></div>
      <div class="row"><span>Board Only Advanced</span><span>90</span><span>130</span><span>150</span><span>180</span><span>200</span></div>
    </div>
    <div class="group">
      <div class="row"><span>Pants &amp; Jacket</span><span>50</span><span>60</span><span>70</span><span>85</span><span>95</span></div>
      <div class="row"><span>Pants Only</span><span>30</span><span>45</span><span>50</span><span>60</span><span>70</span></div>
      <div class="row"><span>Jacket Only</span><span>30</span><span>45</span><span>50</span><span>60</span><span>70</span></div>
      <div class="row"><span>Boots Only</span><span>30</span><span>45</span><span>55</span><span>70</span><span>80</span></div>
      <div class="row"><span>Wrist Guards</span><span>15</span><span>20</span><span>25</span><span>30</span><span>40</span></div>
      <div class="row"><span>Helmets</span><span>20</span><span>25</span><span>30</span><span>40</span><span>50</span></div>
    </div>
    <div class="group">
      <div class="row"><span>Skis &amp; Stocks &amp; Boots Standard</span><span>60</span><span>90</span><span>110</span><span>120</span><span>140</span></div>
      <div class="row"><span>Skis &amp; Stocks &amp; Boots Premium</span><span>80</span><span>110</span><span>130</span><span>150</span><span>180</span></div>
      <div class="row"><span>Skis &amp; Stocks Standard</span><span>50</span><span>75</span><span>95</span><span>110</span><span>125</span></div>
      <div class="row"><span>Skis &amp; Stocks Premium</span><span>65</span><span>95</span><span>115</span><span>135</span><span>150</span></div>
      <div class="row"><span>Ski Boots Only</span><span>30</span><span>45</span><span>55</span><span>70</span><span>80</span></div>
      <div class="row"><span>Stocks Only</span><span>15</span><span>20</span><span>25</span><span>30</span><span>35</span></div>
    </div>
    <div class="group last">
      <div class="row"><span>Walking Boots</span><span>15</span><span>20</span><span>25</span><span>30</span><span>35</span></div>
      <div class="row"><span>Tobogans</span><span>15</span><span>20</span><span>25</span><span>30</span><span>35</span></div>
      <div class="row"><span>Chains</span><span>40</span><span>50</span><span>55</span><span>60</span><span>65</span></div>
    </div>
  </section>

  <section class="price-table child">
    <div class="row table-head"><span>Child</span><span>1 Day</span><span>2 Day</span><span>3 Day</span><span>4/5 Day</span><span>5 Day</span><span>6/7 Day</span></div>
    <div class="group first">
      <div class="row"><span>Board &amp; Boots Standard</span><span>40</span><span>65</span><span>75</span><span>90</span><span>90</span><span>100</span></div>
      <div class="row"><span>Board Only Standard</span><span>35</span><span>50</span><span>65</span><span>80</span><span>80</span><span>90</span></div>
    </div>
    <div class="group">
      <div class="row"><span>Pants &amp; Jacket</span><span>30</span><span>40</span><span>45</span><span>50</span><span>50</span><span>60</span></div>
      <div class="row"><span>Pants Only</span><span>20</span><span>25</span><span>30</span><span>40</span><span>40</span><span>50</span></div>
      <div class="row"><span>Jacket Only</span><span>20</span><span>25</span><span>30</span><span>40</span><span>40</span><span>50</span></div>
    </div>
    <div class="group">
      <div class="row"><span>Boots Only</span><span>20</span><span>25</span><span>35</span><span>45</span><span>45</span><span>55</span></div>
      <div class="row"><span>Wrist Guards</span><span>15</span><span>20</span><span>25</span><span>30</span><span>30</span><span>40</span></div>
      <div class="row"><span>Helmets</span><span>20</span><span>25</span><span>30</span><span>40</span><span>40</span><span>50</span></div>
    </div>
    <div class="group">
      <div class="row"><span>Skis &amp; Stocks &amp; Boots Standard</span><span>40</span><span>65</span><span>75</span><span>90</span><span>90</span><span>100</span></div>
      <div class="row"><span>Skis &amp; Stocks Standard</span><span>35</span><span>50</span><span>65</span><span>80</span><span>80</span><span>90</span></div>
      <div class="row"><span>Ski Boots Only</span><span>20</span><span>25</span><span>35</span><span>45</span><span>45</span><span>55</span></div>
      <div class="row"><span>Stocks Only</span><span>15</span><span>20</span><span>25</span><span>30</span><span>30</span><span>35</span></div>
    </div>
    <div class="group last">
      <div class="row"><span>Walking Boots</span><span>15</span><span>20</span><span>25</span><span>30</span><span>30</span><span>35</span></div>
      <div class="row"><span>Tobogans</span><span>15</span><span>20</span><span>25</span><span>30</span><span>30</span><span>35</span></div>
    </div>
  </section>

  <footer class="offer-band">
    <p class="offer-lead">PRESENT THIS BROCHURE FOR</p>
    <p class="offer-value">20% OFF HIRE</p>
    <div class="brand-row">
      <div class="brand-mark pink"><span class="brand-dot"></span><span>MAPLETON<br>DRIFT HIRE</span></div>
      <div class="brand-mark white"><span class="brand-dot"></span><span>MAPLETON<br>DRIFT HIRE</span></div>
      <div class="brand-mark blue"><span class="brand-dot"></span><span>MAPLETON<br>DRIFT HIRE</span></div>
    </div>
  </footer>

</main>
</body>
</html>
```